Ridgeway Ore Advisory Business Card

Ridgeway Ore Advisory is a company that provides consulting services to the Mining Industry.

Whilst Ridgeway Ore Advisory is an Australian based company its client base is the global mining industry.

The essence of Ridgeway Ore Advisory is its a can do organisation that can make a difference to its clients by providing quality assistance and form lasting relationships.
Updates

Target Market(s)

The global Mining Industry.

Industry/Entity Type

Mining

Font styles to use
Serif

Colors

Designer to choose colors to be used in the design.

Requirements
Nice to have
• My thinking is the card would look good in black given the logo.

I would like to see written on the back side of the card " Providing Metallurgical, Management and Corporate Services to the Mining Industry"

```html
<!DOCTYPE html>
<html lang="en">
<head>
<meta charset="utf-8">
<title>Ridgeway Ore Advisory – Business Card</title>
<link href="https://fonts.googleapis.com/css2?family=Open+Sans:wght@300;400;700&display=swap" rel="stylesheet">
<style>
  :root {
    --canvas: #d9d7d3;
    --card-black: #07030a;
    --card-white: #ffffff;
    --accent: #f5a01a;
    --ink: #2a2a2a;
    --ink-soft: #444444;
  }
  * { box-sizing: border-box; margin: 0; padding: 0; }
  html, body {
    width: 1200px; height: 902px; overflow: hidden;
    background: var(--canvas);
    font-family: "Open Sans", Arial, sans-serif;
  }
  .stage {
    position: relative; width: 1200px; height: 902px;
    display: flex; justify-content: center; align-items: center; gap: 90px;
  }
  .card {
    position: relative; width: 380px; height: 600px;
    background: var(--card-black);
    box-shadow: 0 10px 30px rgba(0,0,0,0.25);
    overflow: hidden;
  }
  .card-front .brand {
    position: absolute; left: 0; right: 0; top: 50%;
    transform: translateY(-50%);
    display: flex; align-items: center; justify-content: center; gap: 10px;
  }
  .brand-dot {
    width: 12px; height: 12px; border-radius: 50%; background: var(--accent);
  }
  .brand-name {
    color: var(--accent); font-weight: 700; font-size: 19px;
    letter-spacing: 0.5px; text-transform: uppercase;
  }
  .card-back .top {
    position: absolute; left: 0; right: 0; top: 0; height: 270px;
    background: var(--card-black);
  }
  .card-back .top .brand {
    position: absolute; left: 0; right: 0; top: 110px;
    display: flex; align-items: center; justify-content: center; gap: 8px;
  }
  .card-back .top .brand-name { font-size: 15px; }
  .card-back .bottom {
    position: absolute; left: 0; right: 0; top: 270px; bottom: 0;
    background: var(--card-white);
  }
  .notch {
    position: absolute; left: 56px; top: 262px;
    width: 16px; height: 16px; border-radius: 50%;
    background: var(--card-white);
  }
  .identity { position: absolute; left: 150px; top: 30px; }
  .person-name { font-size: 30px; font-weight: 400; color: var(--ink); line-height: 1; }
  .person-title { font-size: 15px; color: var(--ink-soft); margin-top: 4px; margin-left: -10px; }
  .contacts { position: absolute; left: 90px; top: 125px; list-style: none; }
  .contacts li {
    display: flex; align-items: center; gap: 10px;
    font-size: 14px; color: var(--ink-soft); margin-bottom: 14px;
  }
  .icon {
    width: 22px; height: 22px; border-radius: 50%; background: var(--accent);
    display: flex; align-items: center; justify-content: center; flex: none;
  }
  .icon svg { width: 13px; height: 13px; }
</style>
</head>
<body>
<main class="stage">
  <section class="card card-front" aria-label="Card front">
    <div class="brand">
      <span class="brand-dot"></span>
      <span class="brand-name">Ridgeway Ore Advisory</span>
    </div>
  </section>

  <section class="card card-back" aria-label="Card back">
    <div class="top">
      <div class="brand">
        <span class="brand-dot"></span>
        <span class="brand-name">Ridgeway Ore Advisory</span>
      </div>
    </div>
    <div class="bottom">
      <div class="identity">
        <p class="person-name">Name</p>
        <p class="person-title">Title</p>
      </div>
      <ul class="contacts">
        <li>
          <span class="icon"><svg viewBox="0 0 24 24"><path fill="#fff" d="M6.6 10.8a15 15 0 0 0 6.6 6.6l2.2-2.2c.3-.3.7-.4 1-.2 1.1.4 2.3.6 3.6.6.6 0 1 .4 1 1V20c0 .6-.4 1-1 1A17 17 0 0 1 3 4c0-.6.4-1 1-1h3.5c.6 0 1 .4 1 1 0 1.3.2 2.5.6 3.6.1.3 0 .7-.2 1z"/></svg></span>
          xxx.xxx.xxxx
        </li>
        <li>
          <span class="icon"><svg viewBox="0 0 24 24"><path fill="#fff" d="M3 5h18v14H3z"/><path fill="none" stroke="#f5a01a" stroke-width="2" d="M3 6l9 7 9-7"/></svg></span>
          email@email.com
        </li>
        <li>
          <span class="icon"><svg viewBox="0 0 24 24"><path fill="#fff" d="M12 2a7 7 0 0 0-7 7c0 5 7 13 7 13s7-8 7-13a7 7 0 0 0-7-7zm0 9.5A2.5 2.5 0 1 1 12 6.5a2.5 2.5 0 0 1 0 5z"/></svg></span>
          Address
        </li>
        <li>
          <span class="icon"><svg viewBox="0 0 24 24"><g fill="none" stroke="#fff" stroke-width="2"><circle cx="12" cy="12" r="9"/><path d="M3 12h18M12 3c3 3 3 15 0 18M12 3c-3 3-3 15 0 18"/></g></svg></span>
          www.web.com
        </li>
      </ul>
    </div>
    <span class="notch"></span>
  </section>
</main>
</body>
</html>
```